Email Signature Block Design for Law Firm

I would like you to create a similar signature block for my law firm . I saw the email signature block attached as image002.png and wanted a similar design for my law firm. I want to be able to swap the portraits for each of my staff from the final design. Our law firm colors are black, gold, white, red.

Industry/Entity Type

Law

Requirements
Nice to have
• i like the red circle in around the photo in the 8 copper bench design. The 9 Copper Bench desgn is what inspired me to have a signature block design for my firm.

```html
<!DOCTYPE html>
<html lang="en">
<head>
<meta charset="utf-8">
<title>The Halbrook Firm – Email Signature</title>
<link rel="stylesheet" href="https://fonts.googleapis.com/css2?family=Cinzel:wght@500;600&family=Poppins:wght@400;600&display=swap">
<style>
  :root {
    --page: #e2e2e2;
    --ink: #0d0b0a;
    --gold: #e0a02a;
    --gold-deep: #c98b1c;
    --white: #ffffff;
    --line: rgba(224,160,42,0.7);
  }
  * { margin: 0; padding: 0; box-sizing: border-box; }
  html, body { width: 1200px; height: 600px; overflow: hidden; background: var(--page); }
  .signature {
    position: absolute; left: 75px; top: 169px; width: 1051px; height: 247px;
    overflow: hidden; color: var(--white); font-family: 'Poppins', sans-serif;
  }
  .signature__backdrop {
    position: absolute; inset: 0;
    background:
      radial-gradient(ellipse at 30% 70%, rgba(70,42,22,0.55), transparent 55%),
      radial-gradient(ellipse at 80% 20%, rgba(80,55,30,0.45), transparent 50%),
      linear-gradient(90deg, #0a0807 0%, #1a120d 45%, #120c09 75%, #221a14 100%);
  }
  .firm { position: absolute; left: 118px; top: 69px; }
  .firm__name {
    font-family: 'Cinzel', serif; font-weight: 600; font-size: 24px;
    letter-spacing: 0.5px; white-space: nowrap; line-height: 1;
  }
  .firm__name small { font-size: 15px; }
  .firm__tagline {
    display: flex; align-items: center; gap: 6px; margin-top: 8px;
    font-family: 'Poppins', sans-serif; font-weight: 600; font-size: 10px;
    letter-spacing: 7.5px; white-space: nowrap;
  }
  .firm__tagline::before, .firm__tagline::after {
    content: ""; height: 1px; width: 36px; background: var(--white);
  }
  .follow { position: absolute; left: 41px; top: 174px; display: flex; align-items: center; }
  .follow__label {
    font-family: 'Poppins', sans-serif; font-weight: 600; font-size: 18px;
    letter-spacing: 2px; margin-right: 22px; white-space: nowrap;
  }
  .follow__links { display: flex; gap: 18px; }
  .follow__dot { width: 21px; height: 21px; border-radius: 50%; background: var(--gold); }
  .portrait {
    position: absolute; left: 432px; top: 30px; width: 186px; height: 186px;
    border-radius: 50%; border: 8px solid var(--gold); overflow: hidden;
    background: linear-gradient(180deg, #f4f4f4 0%, #ffffff 40%, #1b1b1f 75%, #111 100%);
  }
  .contact { position: absolute; left: 660px; top: 36px; width: 270px; }
  .contact__name {
    font-family: 'Cinzel', serif; font-weight: 500; font-size: 29px;
    color: var(--gold); white-space: nowrap; line-height: 1;
  }
  .contact__role { font-size: 15px; margin-top: 2px; line-height: 1.3; }
  .contact__rule { height: 1px; background: var(--line); margin-top: 6px; margin-bottom: 10px; }
  .contact__list { list-style: none; font-size: 14px; line-height: 1.22; }
  .contact__list li { display: flex; align-items: flex-start; gap: 8px; margin-bottom: 5px; white-space: nowrap; }
  .contact__list li.address { margin-bottom: 3px; }
  .contact__icon { width: 11px; height: 11px; margin-top: 4px; flex: none; }
</style>
</head>
<body>
  <section class="signature">
    <div class="signature__backdrop" role="img" aria-label="Dim courtroom background with gavel, scales of justice and bookshelves in dark brown tones"></div>

    <div class="firm">
      <div class="firm__name">The Halbrook Firm, <small>PLLC</small></div>
      <div class="firm__tagline">Attorneys At Law</div>
    </div>

    <div class="follow">
      <span class="follow__label">FOLLOW US ON</span>
      <div class="follow__links">
        <span class="follow__dot" aria-label="Social link"></span>
        <span class="follow__dot" aria-label="Social link"></span>
        <span class="follow__dot" aria-label="Social link"></span>
        <span class="follow__dot" aria-label="Social link"></span>
        <span class="follow__dot" aria-label="Social link"></span>
      </div>
    </div>

    <div class="portrait" role="img" aria-label="Portrait of the attorney in a dark suit, arms crossed"></div>

    <div class="contact">
      <div class="contact__name">Marcus D. Halbrook</div>
      <div class="contact__role">PERSONAL INJURY LAWYER</div>
      <div class="contact__rule"></div>
      <ul class="contact__list">
        <li>
          <svg class="contact__icon" viewBox="0 0 12 12"><circle cx="6" cy="6" r="6" fill="var(--gold)"/><path d="M3.6 3.2l1.2-.4.7 1.5-.7.5c.4.9 1 1.5 1.9 1.9l.5-.7 1.5.7-.4 1.2C6.2 8.1 3.9 5.8 3.6 3.2z" fill="#1a120d"/></svg>
          <span>555-014-2290</span>
        </li>
        <li>
          <svg class="contact__icon" viewBox="0 0 12 12"><circle cx="6" cy="6" r="6" fill="var(--gold)"/><rect x="3" y="4" width="6" height="4" fill="none" stroke="#1a120d" stroke-width="0.9"/><path d="M3 4l3 2.2L9 4" fill="none" stroke="#1a120d" stroke-width="0.9"/></svg>
          <span>marcus@halbrookfirm.com</span>
        </li>
        <li class="address">
          <svg class="contact__icon" viewBox="0 0 12 12"><path d="M6 0.5a4.2 4.2 0 0 1 4.2 4.2C10.2 7.6 6 11.5 6 11.5S1.8 7.6 1.8 4.7A4.2 4.2 0 0 1 6 .5z" fill="var(--gold)"/><circle cx="6" cy="4.7" r="1.6" fill="#1a120d"/></svg>
          <span>412 N Harbor Ave., Suite 118<br>Bayview, FL 32000</span>
        </li>
        <li>
          <svg class="contact__icon" viewBox="0 0 12 12"><circle cx="6" cy="6" r="5.5" fill="var(--gold)"/><g fill="none" stroke="#1a120d" stroke-width="0.7"><circle cx="6" cy="6" r="3.2"/><ellipse cx="6" cy="6" rx="1.4" ry="3.2"/><path d="M2.8 6h6.4"/></g></svg>
          <span>www.halbrookfirm.com</span>
        </li>
      </ul>
    </div>
  </section>
</body>
</html>
```